Visitenkarten für ein Metallverarbeitsungsbetrieb
Zielgruppe
Metallverarbeitsungsbetrieb
spezialisiert auf Lasern
Aufgabenstellung
Passend zu unseren Logo und in den Farben, schlicht dennoch besonders

```html
<!DOCTYPE html>
<html lang="de">
<head>
<meta charset="utf-8">
<title>Visitenkarte – Nordstrahl Laser GmbH</title>
<link href="https://fonts.googleapis.com/css2?family=Barlow+Condensed:wght@400;500&display=swap" rel="stylesheet">
<style>
  :root {
    --bg: #cfe3f1;
    --card: #ffffff;
    --brand-blue: #1a7db5;
    --text-grey: #626468;
    --shadow: rgba(40, 50, 60, 0.35);
  }
  * { margin: 0; padding: 0; box-sizing: border-box; }
  html, body {
    width: 1200px;
    height: 1200px;
    overflow: hidden;
    background: var(--bg);
    font-family: "Barlow Condensed", "Arial Narrow", sans-serif;
  }
  .card {
    position: absolute;
    left: 210px;
    width: 776px;
    height: 444px;
    background: var(--card);
    box-shadow: 0 6px 18px var(--shadow);
  }
  .card--front { top: 117px; }
  .card--back { top: 592px; }

  .rule {
    position: absolute;
    left: 0;
    right: 0;
    height: 2px;
    background: var(--brand-blue);
  }
  .card--front .rule { top: 298px; }
  .card--back .rule { top: 297px; }

  .brand {
    position: absolute;
    left: 76px;
    top: 130px;
    display: flex;
    align-items: center;
    gap: 18px;
  }
  .brand__mark {
    width: 44px;
    height: 44px;
    background: var(--brand-blue);
  }
  .brand__name {
    font-size: 44px;
    font-weight: 500;
    color: var(--text-grey);
    line-height: 1;
    letter-spacing: 0.5px;
  }

  .text {
    position: absolute;
    color: var(--text-grey);
    font-size: 27px;
    line-height: 27px;
    font-weight: 400;
    white-space: nowrap;
  }
  .tagline--1 { left: 83px; top: 326px; }
  .tagline--2 { left: 84px; top: 371px; }

  .person-name {
    position: absolute;
    left: 86px;
    top: 213px;
    font-size: 46px;
    line-height: 46px;
    font-weight: 400;
    color: var(--brand-blue);
    letter-spacing: 0.5px;
  }

  .address--city { left: 83px; top: 333px; }
  .address--street { left: 82px; top: 372px; }

  .divider {
    position: absolute;
    left: 387px;
    top: 330px;
    width: 2px;
    height: 80px;
    background: var(--brand-blue);
  }

  .contact--phone { left: 461px; top: 333px; letter-spacing: 0.6px; }
  .contact--mail { left: 463px; top: 372px; letter-spacing: 1.6px; }
</style>
</head>
<body>
  <section class="card card--front">
    <div class="brand">
      <span class="brand__mark"></span>
      <span class="brand__name">Nordstrahl Laser GmbH</span>
    </div>
    <div class="rule"></div>
    <p class="text tagline--1">Metallverarbeitungsbetrieb</p>
    <p class="text tagline--2">Spezialisiert auf Lasern</p>
  </section>

  <section class="card card--back">
    <h1 class="person-name">YOUR NAME</h1>
    <div class="rule"></div>
    <p class="text address--city">City name, Your Country</p>
    <p class="text address--street">1234 Street name</p>
    <div class="divider"></div>
    <p class="text contact--phone">P:&nbsp; (123) 456789</p>
    <p class="text contact--mail">name@yourcompany.de</p>
  </section>
</body>
</html>
```